Quorvex business card design

create modern and tech looking business card that is clean but effectively communciates that we are a cloud communications company.
Should have at minimum:
Employee Name
Postion
Phone Number
Email
website
create modern and tech looking business card that is clean but effectively communciates that we are a cloud communications company. We have two logo color schemes (attached) so would like to see designs both ways
Should have at minimum:
Employee Name
Postion
Phone Number
Email
website

```html
<!DOCTYPE html>
<html lang="en">
<head>
<meta charset="utf-8">
<title>Quorvex business card</title>
<link href="https://fonts.googleapis.com/css2?family=Open+Sans:wght@400;600&display=swap" rel="stylesheet">
<style>
  :root {
    --stage: #1b1b1b;
    --card: #232323;
    --card-edge: #2e2e2e;
    --cyan: #2bb9dc;
    --white: #f2f2f2;
    --muted: #d6d6d6;
  }
  * { box-sizing: border-box; margin: 0; padding: 0; }
  html, body { width: 1200px; height: 900px; overflow: hidden; background: var(--stage); }
  body {
    font-family: "Open Sans", Arial, sans-serif;
    display: flex; flex-direction: column; align-items: center; justify-content: center; gap: 44px;
  }
  .card {
    width: 700px; height: 400px; background: linear-gradient(135deg, var(--card) 0%, #2a2a2a 100%);
    border: 1px solid var(--card-edge); position: relative;
  }
  .wordmark {
    display: flex; align-items: center; gap: 14px; color: var(--white);
    font-weight: 600; letter-spacing: 4px; text-transform: uppercase;
  }
  .wordmark__dot { width: 16px; height: 16px; background: var(--cyan); }
  .card--front .wordmark { position: absolute; left: 50%; top: 42%; transform: translate(-50%, -50%); font-size: 44px; }
  .card--front .web {
    position: absolute; bottom: 38px; width: 100%; text-align: center;
    font-size: 15px; letter-spacing: 2px; color: var(--white);
  }
  .web__name { color: var(--cyan); }
  .card--back { display: flex; align-items: center; }
  .card--back .wordmark { font-size: 32px; width: 330px; justify-content: center; }
  .divider { width: 2px; height: 210px; background: var(--cyan); }
  .details { padding-left: 34px; color: var(--white); }
  .details__name { color: var(--cyan); font-size: 24px; text-transform: uppercase; letter-spacing: 1px; line-height: 1; }
  .details__role { font-size: 19px; margin-bottom: 20px; }
  .details__address { font-size: 17px; letter-spacing: 1px; line-height: 1.3; margin-bottom: 18px; }
  .contact { list-style: none; font-size: 17px; letter-spacing: 1px; line-height: 1.5; }
  .contact li { display: flex; align-items: center; gap: 12px; }
  .contact svg { width: 16px; height: 16px; flex: none; }
</style>
</head>
<body>
  <section class="card card--front">
    <div class="wordmark"><span class="wordmark__dot"></span>Quorvex</div>
    <p class="web">www.<span class="web__name">quorvex</span>.com</p>
  </section>

  <section class="card card--back">
    <div class="wordmark"><span class="wordmark__dot"></span>Quorvex</div>
    <div class="divider"></div>
    <div class="details">
      <p class="details__name">Dana Whitfield</p>
      <p class="details__role">Founder</p>
      <p class="details__address">4870 Cedar Lane,<br>Suite Tempe 85281</p>
      <ul class="contact">
        <li>
          <svg viewBox="0 0 16 16" aria-hidden="true"><rect x="4" y="1" width="8" height="14" rx="1.5" fill="none" stroke="#2bb9dc" stroke-width="1.6"/></svg>
          0427 593 618
        </li>
        <li>
          <svg viewBox="0 0 16 16" aria-hidden="true"><rect x="1" y="3" width="14" height="10" fill="#2bb9dc"/><path d="M1 3l7 6 7-6" fill="none" stroke="#232323" stroke-width="1.4"/></svg>
          info@danawhitfield.com
        </li>
        <li>
          <svg viewBox="0 0 16 16" aria-hidden="true"><circle cx="7" cy="7" r="4.5" fill="none" stroke="#2bb9dc" stroke-width="2"/><path d="M10.5 10.5L15 15" stroke="#2bb9dc" stroke-width="2.2"/></svg>
          www.quorvex.com
        </li>
      </ul>
    </div>
  </section>
</body>
</html>
```